Business card design for online Mandarin Learning School

We need a business card design for our online language learning school called "Sunny Kite Academy for Mandarin Learning". Our existing website is https://www.sunnykiteacademy.com
We have our logo already. We would like to see our business card design that can make our online teaching services to be innovative, young, energetic and fun to learn. Prefer to have a certain level of color matching with our website. Apart from "Sunny Kite Academy", need to specifically state "for Mandarin Learning" as well on the business card.

```html
<!DOCTYPE html>
<html lang="en">
<head>
<meta charset="utf-8">
<title>Sunny Kite Academy for Mandarin Learning – Business Card</title>
<link href="https://fonts.googleapis.com/css2?family=Open+Sans:wght@400;600;700&display=swap" rel="stylesheet">
<style>
  :root {
    --bg: #2a2a2c;
    --teal: #1fb0bd;
    --coral: #e86a6a;
    --grey: #8f9093;
    --ink: #3c3c3e;
    --rule: #4a4a4a;
    --white: #ffffff;
  }
  * { box-sizing: border-box; margin: 0; padding: 0; }
  html, body { width: 1200px; height: 885px; overflow: hidden; }
  body {
    background: var(--bg);
    font-family: "Open Sans", Arial, sans-serif;
    position: relative;
  }
  .card {
    position: absolute;
    width: 620px;
    height: 354px;
    border-radius: 2px;
    box-shadow: 0 10px 28px rgba(0,0,0,0.45);
    overflow: hidden;
  }
  .brand-dot {
    width: 16px; height: 16px; border-radius: 50%;
    background: var(--coral);
    flex: none;
  }
  .brand-name { line-height: 1.25; }
  .brand-name span { display: block; }

  /* Back side */
  .card-back {
    left: 150px; top: 58px;
    background: linear-gradient(135deg, #f4f4f4 0%, #c9c9c9 40%, #9d9d9d 100%);
  }
  .card-back .brand {
    position: absolute;
    left: 0; right: 0; top: 112px;
    display: flex; justify-content: center; align-items: center; gap: 14px;
    color: var(--teal);
    font-size: 26px; font-weight: 600; letter-spacing: 1px;
    text-align: center;
  }
  .card-back .web {
    position: absolute;
    left: 0; right: 0; top: 218px;
    text-align: center;
    color: var(--white);
    font-size: 15px; letter-spacing: 5px;
  }

  /* Front side */
  .card-front {
    left: 430px; top: 473px;
    background: var(--white);
  }
  .card-front .brand {
    position: absolute;
    right: 56px; top: 58px;
    display: flex; align-items: center; gap: 12px;
    color: var(--teal);
    font-size: 19px; font-weight: 600; letter-spacing: 1px;
    text-align: right;
  }
  .card-front .brand .brand-dot { width: 14px; height: 14px; }
  .top-rule {
    position: absolute;
    left: 240px; right: 56px; top: 132px;
    border-top: 1px solid var(--rule);
  }
  .person { position: absolute; left: 40px; top: 180px; }
  .person-name {
    color: var(--teal); font-size: 22px; font-weight: 700; line-height: 1.1;
  }
  .person-role {
    color: var(--coral); font-size: 14px; line-height: 1.3;
  }
  .person-rule {
    position: absolute; left: 40px; top: 236px; width: 290px;
    border-top: 1px solid var(--rule);
  }
  .contacts {
    position: absolute; left: 44px; top: 244px;
    list-style: none;
    color: var(--ink); font-size: 13.5px; line-height: 19px;
  }
  .contacts li { display: flex; align-items: center; gap: 12px; }
  .contacts svg { width: 14px; height: 14px; fill: var(--teal); flex: none; }
  .address {
    position: absolute; right: 40px; top: 206px;
    text-align: right;
    color: var(--ink); font-size: 13.5px; line-height: 18px;
  }
  .bands { position: absolute; left: 0; bottom: 0; width: 620px; height: 80px; }
  .band-web {
    position: absolute; right: 24px; bottom: 22px;
    color: var(--white); font-size: 13px;
  }
</style>
</head>
<body>

  <section class="card card-back" aria-label="Business card back">
    <div class="brand">
      <span class="brand-dot"></span>
      <p class="brand-name"><span>Sunny Kite Academy</span><span>for Mandarin Learning</span></p>
    </div>
    <p class="web">www.sunnykiteacademy.com</p>
  </section>

  <section class="card card-front" aria-label="Business card front">
    <div class="brand">
      <span class="brand-dot"></span>
      <p class="brand-name"><span>SUNNY KITE ACADEMY</span><span>FOR MANDARIN LEARNING</span></p>
    </div>
    <div class="top-rule"></div>

    <div class="person">
      <p class="person-name">LENA MARSH</p>
      <p class="person-role">PRESIDENT</p>
    </div>
    <div class="person-rule"></div>

    <ul class="contacts">
      <li>
        <svg viewBox="0 0 16 16" aria-hidden="true"><path d="M1 5c0-2 2-3 7-3s7 1 7 3v1h-3V5H4v1H1z"/><rect x="3" y="7" width="10" height="7" rx="1"/></svg>
        555 0142 7781
      </li>
      <li>
        <svg viewBox="0 0 16 16" aria-hidden="true"><path d="M4 1h8v14H4z M5.5 2.5v9h5v-9z" fill-rule="evenodd"/></svg>
        555 0196 2430
      </li>
      <li>
        <svg viewBox="0 0 16 16" aria-hidden="true"><rect x="4" y="1" width="8" height="5"/><rect x="1" y="6" width="14" height="6" rx="1"/><rect x="4" y="11" width="8" height="4"/></svg>
        555 0173 9914
      </li>
      <li>
        <svg viewBox="0 0 16 16" aria-hidden="true"><path d="M1 3h14v10H1z"/><path d="M1 3l7 6 7-6" fill="none" stroke="#fff" stroke-width="1.4"/></svg>
        lena@sunnykiteacademy.com
      </li>
    </ul>

    <div class="address">
      <p>1270 Orchard Lane</p>
      <p>Maple Hill, NY 12345</p>
    </div>

    <svg class="bands" viewBox="0 0 620 80" aria-hidden="true">
      <polygon points="0,60 172,60 166,68 0,68" fill="var(--grey)"/>
      <polygon points="176,60 370,60 392,26 404,26 378,68 170,68" fill="var(--teal)"/>
      <polygon points="0,72 382,72 412,24 620,24 620,80 0,80" fill="var(--coral)"/>
    </svg>
    <p class="band-web">www.sunnykiteacademy.com</p>
  </section>

</body>
</html>
```